Modern & Fresh Sumeray Book Cover

Need a creative e-book cover for my book.

Title: Get Sumeray Sorted
Subtitle: Learn How To Easily Choose & Enroll in the Perfect Coverage at the Perfect Time.

Target Market(s)

60-70 year olds in the United States

Font styles to use
Sans Serif

Colors
9bcb3c
33a6d7

Requirements
Must have
• Must look modern and fresh.
• Use our company colors www.BrovaMint.com

```html
<!DOCTYPE html>
<html lang="en">
<head>
<meta charset="utf-8">
<title>Get Sumeray Sorted – Book Cover</title>
<link rel="stylesheet" href="https://fonts.googleapis.com/css2?family=Jost:wght@400;700&display=swap">
<style>
  :root {
    --stage: #92c5d9;
    --paper: #ffffff;
    --grid: rgba(51, 166, 215, 0.07);
    --brand-green: #9bcb3c;
    --brand-blue: #33a6d7;
    --tint-blue: #e6f3fa;
    --tint-green: #f1f8e6;
    --ink: #3a3a3a;
  }
  html, body {
    margin: 0;
    padding: 0;
    width: 1200px;
    height: 1000px;
    overflow: hidden;
    background: var(--stage);
  }
  .book-cover {
    position: absolute;
    left: 246px;
    top: 0;
    width: 707px;
    height: 1000px;
    background-color: var(--paper);
    background-image:
      linear-gradient(var(--grid) 1px, transparent 1px),
      linear-gradient(90deg, var(--grid) 1px, transparent 1px);
    background-size: 11px 11px;
  }
  .title-backdrop {
    position: absolute;
    left: 60px;
    right: 60px;
    top: 235px;
    height: 380px;
    background: linear-gradient(180deg, var(--tint-blue), var(--tint-green));
    opacity: 0.8;
  }
  .book-title {
    position: absolute;
    left: 0;
    right: 0;
    top: 250px;
    margin: 0;
    text-align: center;
    font-family: "Jost", "Futura", sans-serif;
    font-weight: 700;
    color: var(--brand-blue);
  }
  .book-title span { display: block; }
  .title-line-top { font-size: 96px; line-height: 110px; }
  .title-line-main { font-size: 124px; line-height: 130px; letter-spacing: 1px; }
  .title-line-bottom { font-size: 92px; line-height: 105px; }
  .subtitle {
    position: absolute;
    left: 0;
    right: 0;
    top: 655px;
    margin: 0;
    text-align: center;
    font-family: "Jost", "Futura", sans-serif;
    font-weight: 400;
    font-size: 27px;
    line-height: 33px;
    letter-spacing: 0.3px;
    color: var(--ink);
  }
</style>
</head>
<body>
  <main class="book-cover">
    <div class="title-backdrop" role="img" aria-label="Soft tinted background panel behind the title"></div>
    <h1 class="book-title">
      <span class="title-line-top">Get</span>
      <span class="title-line-main">SUMERAY</span>
      <span class="title-line-bottom">Sorted</span>
    </h1>
    <p class="subtitle">Learn How To Easily Choose &amp; Enroll<br>in the Perfect Coverage at the Perfect Time</p>
  </main>
</body>
</html>
```